Savour and Thrive Wellbeing is being Launched and needs a business card and stationery package

I need a stationery package including business card (primary focus) , letterhead, digital letterhead, envelopes, with compliments slip, A 5 note sheet for the rebranding of my business and launch of my new website. I have a logo, like beige, brown earthy tones with a hint of red. I would also like the option of my letterhead also being printed on recycled paper in another format as well as the traditional letterhead. I do also send my letters to GPs and specialists digitally as well. I like to stand out from the usual stereotype of fruits and vegetables on business cards as I find that quite tacky and stereotypical. I want the business card to capture the essence of my logo as natural, nutrition, enjoyment, nurturing and freedom with food. I have attached the logo, and additional brief sheet on my ideas. Happy to have any background that is complementary to my theme, and what you believe would be catching. Definitely DONT'T like pink, try to pick up the darker colour in the logo please. and think too much black is a little overpowering.

Target Market(s)

clients who are interested in improving their health and wellness. Client 80% females; 20% males

Industry/Entity Type

Health And Wellness

Contact Information for Business Card

I am open to having different backgrounds as well that would complement the logo. Probably less emphasis on the heart out of the logo - just happy to keep that in the logo only please
I am also wanting two business cards - one for the appointments, one for general distribution and media distribution (both need to look consistent though) - but does give opportunity for one of the business cards to be less wordy and more striking. And the front of the business card can certainly stand out with the entire savour and thrive logo and my name and grab the attention of the receiver.
1st business card
on front:
Lorena Whitcombe
Savour and Thrive Wellbeing & logo
Nutritionist and Dietitian
Tarvel Medical Centre
647 Brindle Hill Rd, Quorrel Q 4987
Phone: (07) 3017 2968 Fax: (07) 3156 7209
Mobile: 0400 261 937
www.savourandthrivewellbeing.example.au
lorena@savourandthrivewellbeing.example.au
on back:
next appointment

……………………….. at ……………………… (possibly 4 times)
If you are unable to keep your appointment, please contact us as soon as possible (small font)
2nd business card (needs to be very eye catching and stand out)
on front: Savour and Thrive Wellbeing logo and my name
on back:
Lorena Whitcombe
address
phones, fax, website, email address

Font styles to use
Other font styles liked:
• please refer to logo

Requirements
Must have
• refreshing and simple; new and vibrant - I am rebranding my business after 20 years
• to get a feel of what is the theme - go to my new website (not completed as yet - but you will get a preliminary view) - don't do as google search as blocked - but can put into website header and it will be shown
• www.savourandthrivewellbeing.example.au - but please ignore the colouring of the 4 blocks under the slider on the home page - I am not wanting these colourings - they are getting updated.
Nice to have
• earthy tones, beige, hint of red, fonts to match logo if possible, organic, modern
• get inspiration from my logo please, open to having other backgrounds that complement
Should not have
• no food shots or stereotypical weight/ scales images
• no green, yellow or orange

```html
<!DOCTYPE html>
<html lang="en">
<head>
<meta charset="utf-8">
<title>Savour and Thrive Wellbeing — Business Cards</title>
<link href="https://fonts.googleapis.com/css2?family=Roboto:wght@300;400;500&display=swap" rel="stylesheet">
<style>
  :root {
    --stage: #ece6df;
    --card-cream: #fbf8f4;
    --ink: #3a2a2c;
    --wine: #7e2f45;
    --wine-deep: #5c2032;
    --wine-soft: rgba(126,47,69,0.28);
    --berry-top: #5c2032;
    --berry-mid: #8a3a50;
    --berry-bottom: #6a2639;
    --line-light: rgba(255,240,235,0.75);
    --on-dark: #fbf3ee;
  }
  * { box-sizing: border-box; margin: 0; padding: 0; }
  html, body { width: 1200px; height: 1023px; overflow: hidden; }
  body {
    background: var(--stage);
    font-family: "Roboto", Arial, sans-serif;
    position: relative;
  }
  .card {
    position: absolute;
    width: 740px;
    height: 451px;
    left: 230px;
    border-radius: 22px;
    overflow: hidden;
    box-shadow: 0 6px 18px rgba(60,40,40,0.18);
  }
  /* Front card */
  .card--front { top: 40px; background: var(--card-cream); }
  .petal-motif {
    position: absolute;
    right: -40px; top: -60px;
    width: 470px; height: 330px;
    border-radius: 0 0 50% 60% / 0 0 70% 60%;
    background: radial-gradient(ellipse at 60% 30%, var(--wine-soft) 0%, rgba(126,47,69,0.12) 45%, rgba(251,248,244,0) 72%);
  }
  .brand {
    position: absolute;
    left: 48px; top: 178px;
    display: flex; align-items: center; gap: 14px;
  }
  .brand__dot {
    width: 34px; height: 34px; border-radius: 50%;
    background: var(--wine);
  }
  .brand__name {
    font-weight: 400;
    font-size: 30px;
    color: var(--ink);
    line-height: 1;
  }
  .contact-block {
    position: absolute;
    left: 48px; top: 236px;
  }
  .person__name {
    font-size: 27px; font-weight: 500; color: var(--ink); line-height: 1.1;
  }
  .person__role {
    font-size: 17px; font-weight: 400; color: var(--wine); margin-bottom: 10px;
  }
  .contact-list { list-style: none; }
  .contact-list li {
    display: flex; align-items: center; gap: 10px;
    font-size: 14.5px; color: var(--ink); line-height: 22px;
    letter-spacing: 0.3px;
  }
  .contact-list svg { width: 13px; height: 13px; flex: none; }
  /* Back card */
  .card--back {
    top: 532px;
    background: linear-gradient(160deg, var(--berry-top) 0%, var(--berry-mid) 55%, var(--berry-bottom) 100%);
  }
  .faint-motif {
    position: absolute;
    right: -60px; bottom: -90px;
    width: 430px; height: 320px;
    border-radius: 60% 40% 0 0;
    background: radial-gradient(ellipse at 40% 60%, rgba(40,10,20,0.35) 0%, rgba(40,10,20,0.12) 45%, rgba(40,10,20,0) 72%);
  }
  .appt__title {
    position: absolute;
    left: 0; right: 0; top: 42px; text-align: center;
    font-size: 34px; font-weight: 300; color: var(--on-dark); letter-spacing: 2px;
  }
  .appt__rows {
    position: absolute; left: 60px; top: 130px; width: 620px;
  }
  .appt__row {
    display: flex; align-items: flex-end; gap: 12px;
    height: 56px;
    color: var(--on-dark); font-size: 16px;
  }
  .appt__line {
    flex: 1; border-bottom: 1px dashed var(--line-light); height: 1px; margin-bottom: 4px;
  }
  .appt__line--date { flex: 1.25; }
  .appt__note {
    position: absolute; left: 60px; bottom: 30px;
    font-size: 13.5px; color: var(--on-dark); letter-spacing: 0.3px;
  }
</style>
</head>
<body>

<section class="card card--front" aria-label="Business card front">
  <div class="petal-motif" role="img" aria-label="Large soft petal motif from the brand mark"></div>

  <div class="brand">
    <span class="brand__dot"></span>
    <span class="brand__name">Savour and Thrive Wellbeing</span>
  </div>

  <div class="contact-block">
    <p class="person__name">Lorena Whitcombe</p>
    <p class="person__role">Nutritionist and Dietitian</p>
    <ul class="contact-list">
      <li>
        <svg viewBox="0 0 16 16"><circle cx="8" cy="8" r="7" fill="none" stroke="#7e2f45" stroke-width="1.4"/><path d="M5.5 4.5l1.5 1.5-1 1c.6 1.3 1.7 2.4 3 3l1-1 1.5 1.5-1 1c-2.8-.4-5-2.6-5.5-5.5z" fill="#7e2f45"/></svg>
        (07) 3017 2968
      </li>
      <li>
        <svg viewBox="0 0 16 16"><rect x="4" y="1" width="8" height="14" rx="1.5" fill="#7e2f45"/><rect x="5.5" y="3" width="5" height="8" fill="#fbf8f4"/></svg>
        0400 261 937
      </li>
      <li>
        <svg viewBox="0 0 16 16"><rect x="1" y="6" width="14" height="8" rx="1" fill="#7e2f45"/><rect x="4" y="1" width="8" height="6" fill="#7e2f45"/><rect x="5" y="2" width="6" height="4" fill="#fbf8f4"/></svg>
        (07) 3156 7209
      </li>
      <li>
        <svg viewBox="0 0 16 16"><rect x="1" y="3" width="14" height="10" fill="none" stroke="#7e2f45" stroke-width="1.4"/><path d="M1 3l7 6 7-6" fill="none" stroke="#7e2f45" stroke-width="1.4"/></svg>
        lorena@savourandthrivewellbeing.example.au
      </li>
      <li>
        <svg viewBox="0 0 16 16"><circle cx="8" cy="8" r="7" fill="none" stroke="#7e2f45" stroke-width="1.4"/><path d="M8 3.5a2.8 2.8 0 0 0-2.8 2.8C5.2 8.5 8 12 8 12s2.8-3.5 2.8-5.7A2.8 2.8 0 0 0 8 3.5z" fill="#7e2f45"/></svg>
        647 Brindle Hill Rd, Quorrel Q 4987
      </li>
    </ul>
  </div>
</section>

<section class="card card--back" aria-label="Business card back">
  <div class="faint-motif" role="img" aria-label="Faint petal motif from the brand mark"></div>

  <h2 class="appt__title">Next Appointment</h2>

  <div class="appt__rows">
    <div class="appt__row"><span class="appt__line appt__line--date"></span><span>at</span><span class="appt__line"></span></div>
    <div class="appt__row"><span class="appt__line appt__line--date"></span><span>at</span><span class="appt__line"></span></div>
    <div class="appt__row"><span class="appt__line appt__line--date"></span><span>at</span><span class="appt__line"></span></div>
  </div>

  <p class="appt__note">If you are unable to keep your appointment, please contact us as soon as possible</p>
</section>

</body>
</html>
```